Wedding and event Photography company.

We need a business card design for a photography company based in Singapore named TamKeza. Our core service offering is wedding photojournalism. We would like to see minimalistic designs that use the colour white. The final design should communicate a sense of ease and reliability.

The attached are a couple of visual reference which i found over the web, i hope it will helps.

Project Brief Update (14th July 2014):
- Please refrain from using any images from the website for the design. The laws and regulations over here does not allow me to distribute my client's images. Thanks!

Target Market(s)

Young and middle aged adults aged 24 - 38. With money to spend =D

Industry/Entity Type

Business

Contact Information for Business Card

Name: Dev Lunor
Designation: Head Photographer
Mobile: +65 81749026
Email: jun@tamkeza.example
Website: www.tamkeza.example

Font styles to use
Other font styles liked:
• Baskerville URW

Colors

Designer to choose colors to be used in the design.

Requirements
Must have
• Must include:
• - The brand TamKeza
• - The logo attached
• - Please help to place the brand TamKeza with the logo according to your preferences.
• - Services
• - Wedding Photography
• - Portraiture
• - Photojournalism
Nice to have
• Looking forward to an elegant and simple design. Please see attached examples!
• Please use Serif Fonts
Should not have
• Please refrain from using dark tones for the majority of the design.
• Please refrain from letterpress and embossing.

```html
<!DOCTYPE html>
<html lang="en">
<head>
<meta charset="utf-8">
<title>TamKeza Business Card</title>
<link rel="stylesheet" href="https://fonts.googleapis.com/css2?family=Crimson+Text&family=Open+Sans:wght@400;700&display=swap">
<style>
  :root {
    --backdrop: #525252;
    --card-paper: #faf7f5;
    --ink: #111111;
    --wordmark: #ffffff;
    --mountain-deep: #3e5585;
    --mountain-mid: #8796b8;
    --sky-pale: #e6e4ea;
    --leaf-deep: #2f5a1a;
    --leaf-mid: #6f9a3a;
    --leaf-light: #b4d27a;
  }
  * { margin: 0; padding: 0; box-sizing: border-box; }
  html, body { width: 1200px; height: 900px; overflow: hidden; }
  body {
    background: var(--backdrop);
    position: relative;
    font-family: "Open Sans", Arial, sans-serif;
    color: var(--ink);
  }
  .card {
    position: absolute;
    top: 306px;
    width: 440px;
    height: 271px;
    box-shadow: 3px 4px 6px rgba(0,0,0,0.45);
    overflow: hidden;
  }
  .card-front { left: 149px; background: var(--card-paper); }
  .card-back { left: 608px; }

  .front-photo {
    position: absolute;
    left: 0; top: 0;
    width: 440px; height: 185px;
    background: linear-gradient(100deg, var(--mountain-deep) 0%, var(--mountain-mid) 45%, var(--sky-pale) 80%, #c9cede 100%);
  }
  .logo-mark {
    position: absolute;
    left: 60px; top: 46px;
    width: 58px; height: 58px;
    border: 2px solid var(--wordmark);
    border-radius: 50%;
  }
  .wordmark {
    position: absolute;
    left: 20px; top: 118px;
    font-family: "Crimson Text", Georgia, serif;
    font-size: 42px;
    line-height: 1;
    color: var(--wordmark);
  }
  .holder {
    position: absolute;
    left: 22px; top: 213px;
  }
  .holder-name {
    font-weight: 700;
    font-size: 15px;
    text-transform: uppercase;
    line-height: 1.15;
  }
  .holder-role { font-size: 11.5px; line-height: 1.4; }

  .contacts {
    position: absolute;
    left: 174px; top: 207px;
    list-style: none;
    font-size: 12px;
    line-height: 15.5px;
  }
  .contacts li { display: flex; align-items: center; gap: 6px; }
  .contacts svg { width: 8px; height: 8px; fill: var(--ink); flex: none; }

  .back-photo {
    position: absolute;
    inset: 0;
    background: radial-gradient(ellipse at 60% 45%, var(--leaf-light) 0%, #93b85a 45%, var(--leaf-mid) 80%, var(--leaf-deep) 100%);
  }
  .services {
    position: absolute;
    left: 0; right: 0; bottom: 16px;
    text-align: center;
    font-family: "Crimson Text", Georgia, serif;
    font-size: 14px;
    letter-spacing: 0.5px;
    color: var(--wordmark);
  }
</style>
</head>
<body>
  <section class="card card-front">
    <div class="front-photo" role="img" aria-label="Wedding couple embracing in front of snowy mountains"></div>
    <div class="logo-mark" aria-hidden="true"></div>
    <div class="wordmark">TamKeza</div>
    <div class="holder">
      <div class="holder-name">Dev Lunor</div>
      <div class="holder-role">Head Photographer</div>
    </div>
    <ul class="contacts">
      <li><svg viewBox="0 0 8 8"><path d="M2 0h4v8H2z M2.7 1v5.2h2.6V1z" fill-rule="evenodd"/></svg>+65 81749026</li>
      <li><svg viewBox="0 0 8 8"><path d="M0 1.5h8v5H0z"/><path d="M0 1.5l4 2.8 4-2.8" stroke="#faf7f5" stroke-width="0.8" fill="none"/></svg>jun@tamkeza.example</li>
      <li><svg viewBox="0 0 8 8"><circle cx="4" cy="4" r="3.8"/></svg>www.tamkeza.example</li>
    </ul>
  </section>

  <section class="card card-back">
    <div class="back-photo" role="img" aria-label="Wedding couple embracing on a stone stairway framed by green bamboo"></div>
    <p class="services">Wedding Photography · Portraiture · Photojournalism</p>
  </section>
</body>
</html>
```